The Garden Under the Lantern: A Quiet Pilgrimage

This is a memoir about my breakdown/breakthrough followed by a spiritual awakening in 2012, I found my guru Hemant Sulori Dev, Mother Ayahuasca, and my spiritual mother, Lalu. By 2013, I was headed for a spiritual adventure through India, Southeast India, and Nepal which lasted 14 months. I lived in ashrams, meditated and prayed in temples,, traveled by train and bus, met many enlightened beings and interesting people. During Vipassana, I discovered my true essence- the light of my soul. It is a book of travel, romance, and spiritual growth. My idea is a road lined with temples, etc. I am walking down the road and see myself at the end of the road, facing out, with a bright star in my heart center. I see the colors in muted yellows and other earth-tone hues. Marigolds are used everywhere in the temples to adorn statues and doorways and this speaks to me. The title of the book is about finding out who I am beyond my stories and it is also about how our story will reveal to us who we really are.

Target Market(s)

Spiritual seekers, adventurers, travelers

Industry/Entity Type

Spiritual

Font styles to use
Serif
Sans Serif
Other font styles liked:
• I’m open. I like simplicity

Colors
FFC000
F8CF3A
FAE287
FDF2CF
FEFAEE

Requirements
Must have
• My name: Greta Lunara Ses, Earth tones, pastels, me or a likeness of me, room for ISBN on back cover
Nice to have
• In the photo uploads I drew an idea of what I would like, there is also the idea in the book
Should not have
• I am not a fan of bright colors and that's all I can select here. I like neutral colors, like browns, slate, creams, and whites. This reflects the dusty roads I took throughout my journey.

```html
<!DOCTYPE html>
<html lang="en">
<head>
<meta charset="utf-8">
<title>The Garden Under the Lantern — Book Cover</title>
<link href="https://fonts.googleapis.com/css2?family=Marcellus&family=Cormorant+Garamond:ital,wght@1,500&display=swap" rel="stylesheet">
<style>
  :root {
    --backdrop: #262626;
    --cover-cream: #f2ede7;
    --road-white: #ffffff;
    --ink-taupe: #a59886;
    --figure-sand: #e0d5c8;
    --glow: #fffaf0;
  }
  * { margin: 0; padding: 0; box-sizing: border-box; }
  html, body {
    width: 1200px; height: 1200px; overflow: hidden;
    background: var(--backdrop);
  }
  .cover {
    position: absolute;
    left: 217px; top: 26px;
    width: 765px; height: 1148px;
    background: var(--cover-cream);
    overflow: hidden;
  }
  .cover-art {
    position: absolute; inset: 0;
    width: 765px; height: 1148px;
  }
  .title {
    position: absolute;
    left: 0; right: 0; top: 70px;
    text-align: center;
    font-family: "Marcellus", serif;
    font-weight: 400;
    font-size: 80px;
    line-height: 140px;
    letter-spacing: 0.08em;
    color: var(--ink-taupe);
    text-transform: uppercase;
  }
  .title span { display: block; padding-left: 0.08em; }
  .author {
    position: absolute;
    right: 66px; top: 1066px;
    font-family: "Marcellus", serif;
    font-size: 27px;
    letter-spacing: 0.13em;
    color: var(--ink-taupe);
    text-transform: uppercase;
  }
</style>
</head>
<body>
  <main class="cover">
    <svg class="cover-art" viewBox="0 0 765 1148" xmlns="http://www.w3.org/2000/svg">
      <defs>
        <radialGradient id="heart-glow" cx="0.5" cy="0.38" r="0.6">
          <stop offset="0" stop-color="var(--glow)"/>
          <stop offset="0.35" stop-color="#efe6da"/>
          <stop offset="1" stop-color="var(--figure-sand)"/>
        </radialGradient>
      </defs>

      <polygon class="road" points="0,762 765,657 765,752 0,1148" fill="var(--road-white)"/>

      <rect class="walker-figure" x="60" y="521" width="120" height="475" rx="36"
            fill="var(--figure-sand)" role="img"
            aria-label="Silhouette of a woman walking down the road toward the viewer"/>

      <rect class="radiant-figure" x="665" y="530" width="62" height="209" rx="20"
            fill="url(#heart-glow)" role="img"
            aria-label="Small silhouette of the same woman at the end of the road, a soft light glowing from her heart"/>

      <text class="subtitle" x="206" y="892" transform="rotate(-17.6 206 892)"
            font-family="'Cormorant Garamond', serif" font-style="italic" font-weight="500"
            font-size="46" letter-spacing="7" fill="var(--ink-taupe)">A Quiet Pilgrimage</text>
    </svg>

    <h1 class="title">
      <span>The Garden</span>
      <span>Under</span>
      <span>The</span>
      <span>Lantern</span>
    </h1>

    <p class="author">Greta Lunara Ses</p>
  </main>
</body>
</html>
```